Private Investigation Business Card Design

I need a business card for a new private investigation company named Veltrane Inquiries. I perform mainly surveillance jobs, vehicle repossessions, document serves etc. The final design should aim for a professional look. The logo has a magnifying glass with stick man arms and legs and is in a running action to show the "Veltrane" aspect of the name. If the colour scheme could remain the same as the website www.veltraneinquiries.com.au with silvers,blacks and a couple electric blue highlights.
Business
Contact Information for Business Card
Morgan Kalvane
Veltrane Inquiries
0437862914
PO Box 48, Birchwood NSW 2301
info@veltraneinquiries.com.au
www.veltraneinquiries.com.au

```html
<!DOCTYPE html>
<html lang="en">
<head>
<meta charset="utf-8">
<title>Veltrane Inquiries – Business Card</title>
<link rel="stylesheet" href="https://fonts.googleapis.com/css2?family=Michroma&family=Exo+2:wght@400&display=swap">
<style>
  :root {
    --backdrop: #3b3b3d;
    --card-white: #f7f7f8;
    --card-black: #070707;
    --ink: #111111;
    --silver-light: #e4e5e7;
    --silver-mid: #b9bbbf;
    --silver-dark: #8d9096;
    --electric-blue: #5a9ee6;
  }
  * { box-sizing: border-box; margin: 0; padding: 0; }
  html, body { width: 1200px; height: 900px; overflow: hidden; }
  body {
    background: var(--backdrop);
    position: relative;
    font-family: "Exo 2", Arial, sans-serif;
  }
  .card {
    position: absolute;
    left: 260px;
    width: 680px;
    height: 415px;
    border-radius: 4px;
    overflow: hidden;
    box-shadow: 0 10px 30px rgba(0,0,0,.45);
  }

  /* Back of card */
  .card-back {
    top: 22px;
    background: linear-gradient(115deg, #000 0%, #141414 45%, #2a2a2a 52%, #0b0b0b 60%, #000 100%);
  }
  .card-back .decor-area {
    position: absolute;
    left: 0; top: 70px;
    width: 200px; height: 280px;
    background: radial-gradient(circle at 30% 40%, rgba(230,230,232,.35), rgba(40,40,40,.1) 70%);
  }
  .card-back .brand-name {
    position: absolute;
    right: 60px; top: 170px;
    font-family: "Michroma", Arial, sans-serif;
    font-size: 34px;
    letter-spacing: 2px;
    color: var(--silver-mid);
  }

  /* Front of card */
  .card-front {
    top: 463px;
    background: linear-gradient(135deg, #ffffff 0%, var(--card-white) 55%, #e6e7e9 100%);
  }
  .card-front .brand {
    position: absolute;
    left: 40px; top: 38px;
    display: flex; align-items: center; gap: 12px;
  }
  .card-front .brand-name {
    font-family: "Michroma", Arial, sans-serif;
    font-size: 22px;
    color: var(--silver-dark);
  }
  .card-front .brand-dot {
    width: 14px; height: 14px;
    border-radius: 50%;
    background: var(--silver-mid);
  }
  .holder-name {
    position: absolute;
    left: 40px; top: 120px;
    font-family: "Michroma", Arial, sans-serif;
    font-size: 24px;
    letter-spacing: 1px;
    color: var(--ink);
    text-transform: uppercase;
    font-weight: 400;
  }
  .contact-list {
    position: absolute;
    left: 40px; top: 180px;
    list-style: none;
  }
  .contact-list li {
    display: flex; align-items: center; gap: 12px;
    font-size: 19px;
    color: var(--ink);
    height: 30px;
  }
  .contact-list svg { width: 16px; height: 16px; fill: var(--electric-blue); }
  .decor-area-front {
    position: absolute;
    right: 0; top: 150px;
    width: 240px; height: 200px;
    background: radial-gradient(circle at 70% 40%, rgba(40,40,40,.25), rgba(200,200,200,.08) 70%);
  }
  .base-band { position: absolute; left: 0; bottom: 0; width: 680px; height: 120px; }
  .website {
    position: absolute;
    left: 40px; bottom: 40px;
    display: flex; align-items: center; gap: 12px;
    font-size: 19px;
    color: var(--ink);
  }
  .website svg { width: 16px; height: 16px; }
</style>
</head>
<body>

<section class="card card-back" aria-label="Card back">
  <div class="decor-area" role="img" aria-label="Running magnifying-glass figure decoration"></div>
  <div class="brand-name">Veltrane Inquiries</div>
</section>

<section class="card card-front" aria-label="Card front">
  <div class="brand">
    <span class="brand-name">Veltrane Inquiries</span>
    <span class="brand-dot"></span>
  </div>

  <h1 class="holder-name">Morgan Kalvane</h1>

  <ul class="contact-list">
    <li>
      <svg viewBox="0 0 16 16"><rect x="4" y="1" width="8" height="14" rx="1.5"/><rect x="5.5" y="3" width="5" height="6" fill="#fff"/></svg>
      0437862914
    </li>
    <li>
      <svg viewBox="0 0 16 16"><path d="M8 1a5 5 0 0 0-5 5c0 4 5 9 5 9s5-5 5-9a5 5 0 0 0-5-5zm0 7a2 2 0 1 1 0-4 2 2 0 0 1 0 4z"/></svg>
      PO Box 48, Birchwood NSW 2301
    </li>
    <li>
      <svg viewBox="0 0 16 16"><rect x="1" y="3" width="14" height="10" rx="1"/><path d="M1.5 3.5 8 9l6.5-5.5" stroke="#fff" stroke-width="1.3" fill="none"/></svg>
      info@veltraneinquiries.com.au
    </li>
  </ul>

  <div class="decor-area-front" role="img" aria-label="Running magnifying-glass figure with speed lines"></div>

  <svg class="base-band" viewBox="0 0 680 120" aria-hidden="true">
    <defs>
      <linearGradient id="band-silver" x1="0" y1="0" x2="1" y2="1">
        <stop offset="0" stop-color="#eeeff1"/>
        <stop offset=".5" stop-color="#c9cbcf"/>
        <stop offset="1" stop-color="#f2f2f4"/>
      </linearGradient>
    </defs>
    <polygon points="0,10 450,10 480,50 525,25 680,40 680,120 0,120" fill="url(#band-silver)"/>
    <polyline points="0,10 450,10 480,50 525,25 680,40" fill="none" stroke="var(--electric-blue)" stroke-width="2"/>
  </svg>

  <div class="website">
    <svg viewBox="0 0 16 16"><circle cx="8" cy="8" r="7" fill="var(--electric-blue)"/><path d="M1 8h14M8 1c-3 3.5-3 10.5 0 14M8 1c3 3.5 3 10.5 0 14" stroke="#fff" stroke-width="1" fill="none"/></svg>
    www.veltraneinquiries.com.au
  </div>
</section>

</body>
</html>
```